" Empresa multidisciplinar, focada na reabilitação de pacientes com dor crônica, pós-operatório, reabilitação músculo esquelética em geral. Atendimento com educador físico, fisioterapeuta, médicos "

```html
<!DOCTYPE html>
<html lang="pt-BR">
<head>
<meta charset="UTF-8">
<title>Assinatura de e-mail – MotriVida</title>
<link rel="stylesheet" href="https://fonts.googleapis.com/css2?family=Montserrat:wght@300;400;600&display=swap">
<style>
  :root {
    --bg: #e9e9e9;
    --card: #ffffff;
    --navy: #13223f;
    --gold: #f2c230;
    --ink: #2b2b2b;
    --muted: #555a60;
    --light: #ffffff;
  }
  * { box-sizing: border-box; margin: 0; padding: 0; }
  html, body { width: 1200px; height: 1200px; overflow: hidden; }
  body {
    background: var(--bg);
    font-family: "Montserrat", Arial, sans-serif;
    position: relative;
  }
  .signature {
    position: absolute;
    left: 50px; top: 460px;
    width: 1100px; height: 280px;
    background: var(--card);
    box-shadow: 0 4px 18px rgba(0,0,0,0.12);
    overflow: hidden;
  }
  .brand-panel {
    position: absolute; left: 0; top: 0;
    width: 440px; height: 280px;
  }
  .brand-panel svg { position: absolute; inset: 0; }
  .brand {
    position: absolute; left: 30px; top: 0;
    width: 330px; height: 280px;
    display: flex; align-items: center; justify-content: center;
    gap: 14px;
  }
  .brand-mark {
    width: 40px; height: 40px;
    border-radius: 50%;
    background: var(--light);
    flex: none;
  }
  .brand-name {
    font-weight: 600;
    font-size: 40px;
    line-height: 1;
    color: var(--light);
  }
  .contact {
    position: absolute; left: 490px; top: 28px;
    color: var(--ink);
  }
  .contact-name { font-size: 42px; font-weight: 600; line-height: 48px; }
  .contact-role { font-size: 26px; font-weight: 300; line-height: 30px; color: var(--muted); margin-bottom: 12px; }
  .contact-list { list-style: none; }
  .contact-list li {
    display: flex; align-items: flex-start; gap: 14px;
    font-size: 19px; line-height: 26px; color: var(--ink);
  }
  .contact-list svg { width: 20px; height: 20px; margin-top: 3px; flex: none; fill: var(--ink); }
</style>
</head>
<body>
  <section class="signature" aria-label="Assinatura de e-mail">
    <div class="brand-panel">
      <svg viewBox="0 0 440 280" width="440" height="280" aria-hidden="true">
        <path d="M0 0 H360 Q450 140 360 280 H0 Z" fill="var(--gold)"/>
        <path d="M0 0 H346 Q432 140 346 280 H0 Z" fill="var(--navy)"/>
      </svg>
      <div class="brand">
        <div class="brand-mark"></div>
        <div class="brand-name">MotriVida</div>
      </div>
    </div>

    <div class="contact">
      <h1 class="contact-name">Lívia Andrade</h1>
      <p class="contact-role">Administradora</p>
      <ul class="contact-list">
        <li>
          <svg viewBox="0 0 24 24"><path d="M6.6 10.8a15.1 15.1 0 0 0 6.6 6.6l2.2-2.2c.3-.3.7-.4 1-.2 1.1.4 2.3.6 3.6.6.6 0 1 .4 1 1V20c0 .6-.4 1-1 1A17 17 0 0 1 3 4c0-.6.4-1 1-1h3.5c.6 0 1 .4 1 1 0 1.3.2 2.5.6 3.6.1.3 0 .7-.2 1z"/></svg>
          (99) 9 9999-9999
        </li>
        <li>
          <svg viewBox="0 0 24 24"><circle cx="12" cy="12" r="9" fill="none" stroke="var(--ink)" stroke-width="2.4"/></svg>
          (99) 9 9999-9999
        </li>
        <li>
          <svg viewBox="0 0 24 24"><rect x="3" y="3" width="18" height="18" rx="4"/></svg>
          @motrividareab
        </li>
        <li>
          <svg viewBox="0 0 24 24"><path d="M12 2a7 7 0 0 0-7 7c0 5.2 7 13 7 13s7-7.8 7-13a7 7 0 0 0-7-7zm0 9.5A2.5 2.5 0 1 1 12 6.5a2.5 2.5 0 0 1 0 5z"/></svg>
          <span>Endereço completo, nº 123<br>Estado - UF | CEP 00000-00</span>
        </li>
      </ul>
    </div>
  </section>
</body>
</html>
```